BENEATH THE [HARBOR] OF A DAWN, Mend your road

We are looking for a cover refresh of an existing bestselling book that is going into 3rd edition print this year.
The book is an inspirational as well as educational book that has become recognized as one of the most comprehensive, actionable, personal and financial planning resources available today for families, individuals and business owners alike.
Comprised of three true stories of loss, learning to live and love again and a 30 page checklist at the back of the book it contains tips and strategies for everyone to help them to get their personal and financial lives in order while they can.
The cover must have the following:
1. Appeal to a broad audience/both personal and corporate
2. Include Mara Quellton Bestselling Author
3. Include introduction of a new Afterword
4. 3rd Edition
5. Colors to remain the same – red, black and white
6. The title must remain in caps and the word [HARBOR] must have the brackets around it
We have also added a current copy of the second edition to help you. For your information our website is www.thequelltonhouse.example
Reason: We have narrowed it down to our top 3 designs. We are submitting the covers to our community for them to pick the top cover. Good luck to everyone

```html
<!DOCTYPE html>
<html lang="en">
<head>
<meta charset="utf-8">
<title>Beneath the [Harbor] of a Dawn — Cover</title>
<link rel="stylesheet" href="https://fonts.googleapis.com/css2?family=Kalam:wght@400;700&family=Fjalla+One&display=swap">
<style>
  :root {
    --cover-red: #d51014;
    --ink-black: #0a0a0a;
    --paper-white: #ffffff;
    --frame-width: 26px;
    --art-light: #f6f6f6;
    --art-shade: #d9d6d0;
    --art-gold: #d8b46a;
  }
  html, body {
    margin: 0;
    padding: 0;
    width: 800px;
    height: 1200px;
    overflow: hidden;
    background: var(--paper-white);
  }
  .cover {
    position: relative;
    width: 800px;
    height: 1200px;
    box-sizing: border-box;
    background:
      linear-gradient(to bottom, transparent 5%, var(--ink-black) 9%, var(--ink-black) 87%, transparent 92%) right top / var(--frame-width) 100% no-repeat,
      linear-gradient(to bottom, transparent 53%, var(--ink-black) 57%) left top / var(--frame-width) 100% no-repeat,
      linear-gradient(to right, var(--ink-black) 24%, transparent 34%) left bottom / 100% var(--frame-width) no-repeat,
      var(--cover-red);
  }
  .cover-page {
    position: absolute;
    inset: var(--frame-width);
    background: var(--paper-white);
    overflow: hidden;
  }
  .title {
    margin: 0;
    font-weight: 400;
  }
  .title-script-block {
    position: absolute;
    left: 6px;
    top: 124px;
    width: 306px;
    text-align: right;
    font-family: "Kalam", cursive;
    font-size: 40px;
    line-height: 74px;
    color: var(--ink-black);
    white-space: nowrap;
  }
  .title-script { display: block; }
  .title-keyword {
    position: absolute;
    left: 326px;
    top: 142px;
    font-family: "Fjalla One", sans-serif;
    font-size: 100px;
    line-height: 1;
    letter-spacing: 1px;
    color: var(--cover-red);
    white-space: nowrap;
  }
  .title-keyword .keyword-accent { color: var(--ink-black); }
  .subtitle {
    position: absolute;
    left: 352px;
    top: 262px;
    margin: 0;
    font-family: "Kalam", cursive;
    font-size: 38px;
    line-height: 1;
    color: var(--ink-black);
    white-space: nowrap;
  }
  .cover-art {
    position: absolute;
    left: 12px;
    top: 318px;
    width: 736px;
    height: 470px;
    background:
      radial-gradient(ellipse at 88% 45%, var(--art-gold) 0%, rgba(216,180,106,0) 22%),
      linear-gradient(135deg, var(--paper-white) 20%, var(--art-light) 55%, var(--art-shade) 100%);
  }
  .edition-note {
    position: absolute;
    left: 0;
    right: 0;
    top: 836px;
    margin: 0;
    text-align: center;
    line-height: 1;
  }
  .edition-label {
    display: block;
    font-family: "Fjalla One", sans-serif;
    font-size: 34px;
    letter-spacing: 2px;
    color: var(--cover-red);
    text-transform: uppercase;
  }
  .edition-afterword {
    display: block;
    margin-top: 12px;
    font-family: "Kalam", cursive;
    font-size: 28px;
    color: var(--ink-black);
  }
  .author-credit {
    position: absolute;
    left: 0;
    right: 0;
    top: 982px;
    margin: 0;
    text-align: center;
    font-family: "Fjalla One", sans-serif;
    font-size: 22px;
    letter-spacing: 4px;
    text-transform: uppercase;
    color: var(--cover-red);
  }
  .author-name {
    position: absolute;
    left: 0;
    right: 0;
    top: 1030px;
    margin: 0;
    text-align: center;
    font-family: "Kalam", cursive;
    font-size: 60px;
    line-height: 1;
    color: var(--ink-black);
    word-spacing: 14px;
  }
</style>
</head>
<body>
  <div class="cover">
    <div class="cover-page">
      <h1 class="title">
        <span class="title-script-block">
          <span class="title-script">BENEATH THE</span>
          <span class="title-script">OF A DAWN</span>
        </span>
        <span class="title-keyword">[HAR<span class="keyword-accent">B</span>OR]</span>
      </h1>
      <p class="subtitle">Mend YOUR Road</p>
      <div class="cover-art" role="img" aria-label="Illustration of a gold-nibbed fountain pen drawing a winding ink line with ink drops on white paper"></div>
      <p class="edition-note">
        <span class="edition-label">3rd Edition</span>
        <span class="edition-afterword">With a New Afterword</span>
      </p>
      <p class="author-credit">Bestselling Author</p>
      <p class="author-name">Mara Quellton</p>
    </div>
  </div>
</body>
</html>
```